Residential Construction Design

I'd like a business card that really explains what we do in residential construction. A big name and number, while the other information can be smaller. Since the logo is made up of grays and a teal color, the background may have to stay white? Maybe a subtle gray.(sending 2 different color schemes of the logo for different background color options) I would like a card that just appears "tough" when you look at it.

Industry/Entity Type

Residential

Contact Information for Business Card

Name and logo which will be provided.(Rex Morton Construction, LLC) Rex Morton -Licensed Contractor, Certified Home Inspector. (555) 214-7730 Email: Rmorton_Construction@quellbox.example -Remodeling -Roofs - Siding -Drywall -Decks -Pole Barns -New Construction "Serving Southwest Michigan"

```html
<!DOCTYPE html>
<html lang="en">
<head>
<meta charset="utf-8">
<title>Rex Morton Construction, LLC — Business Card</title>
<link rel="stylesheet" href="https://fonts.googleapis.com/css2?family=Arimo:wght@400;700&display=swap">
<style>
  :root {
    --stage-light: #ffffff;
    --stage-dark: #97989a;
    --card-grey: #e6e7e8;
    --card-white: #ffffff;
    --band: #b9babc;
    --band-soft: #c9cacc;
    --ink: #333436;
    --ink-mid: #58595b;
    --ink-soft: #6d6e70;
    --icon-box: #8c8d8f;
  }
  * { margin: 0; padding: 0; box-sizing: border-box; }
  html, body { width: 1200px; height: 900px; overflow: hidden; }
  body { position: relative; font-family: "Arimo", Arial, sans-serif; color: var(--ink); }
  .stage { position: absolute; left: 0; width: 1200px; height: 450px; }
  .stage--light { top: 0; background: var(--stage-light); }
  .stage--dark { top: 450px; background: var(--stage-dark); }

  .card {
    position: absolute; left: 256px; width: 688px; height: 386px;
    border-radius: 14px; overflow: hidden;
  }
  .card--grey { top: 41px; background: var(--card-grey); }
  .card--white { top: 473px; background: var(--card-white); }

  .phone {
    position: absolute; top: 21px; left: 482px;
    display: flex; align-items: center; gap: 9px;
    font-size: 20px; color: var(--ink-mid);
  }
  .phone__icon { width: 29px; height: 29px; background: var(--icon-box); display: block; }

  .brand {
    position: absolute; top: 62px; left: 149px;
    display: flex; align-items: flex-end; gap: 14px;
  }
  .brand__mark { width: 110px; height: 110px; background: var(--ink-soft); }
  .brand__name {
    font-weight: 700; font-size: 31px; line-height: 1.05;
    color: var(--ink); letter-spacing: 0.5px;
  }

  .band {
    position: absolute; left: 0; bottom: 0; width: 688px; height: 126px;
    background: linear-gradient(120deg, var(--band) 0%, var(--band-soft) 45%, var(--band) 100%);
  }
  .details {
    position: absolute; left: 0; bottom: 0; width: 688px; height: 126px;
    text-align: center; padding-top: 5px; padding-left: 6px;
  }
  .details__name { font-size: 26px; font-weight: 700; color: var(--ink); line-height: 30px; }
  .details__title { font-size: 13px; color: var(--ink); line-height: 16px; }
  .details__email { font-size: 16px; font-weight: 700; color: var(--ink); line-height: 24px; }
  .details__services { font-size: 13px; color: var(--ink); line-height: 15px; }
</style>
</head>
<body>
  <div class="stage stage--light"></div>
  <div class="stage stage--dark"></div>

  <section class="card card--grey">
    <div class="phone">
      <svg class="phone__icon" viewBox="0 0 29 29" aria-hidden="true">
        <rect width="29" height="29" fill="#8c8d8f"/>
        <path d="M10 6 l3 0 l1.5 5 l-2 1.5 c1 2.5 2.5 4 5 5 l1.5 -2 l5 1.5 l0 3 c-8 1 -15 -6 -14 -14z" fill="#333436"/>
      </svg>
      <span>(555) 214-7730</span>
    </div>
    <div class="brand">
      <div class="brand__mark"></div>
      <div class="brand__name">REX MORTON<br>CONSTRUCTION, LLC</div>
    </div>
    <div class="band" role="img" aria-label="Decorative band of overlapping grey angular shapes"></div>
    <div class="details">
      <p class="details__name">Rex Morton</p>
      <p class="details__title">(Licensed Contractor, Certified Home Inspector)</p>
      <p class="details__email">Mail ID: Rmorton_Construction@quellbox.example</p>
      <p class="details__services">Remodeling / Roofs / Siding / Drywall / Decks /<br>Pole Barns / New Construction "Serving Southwest Michigan"</p>
    </div>
  </section>

  <section class="card card--white">
    <div class="phone">
      <svg class="phone__icon" viewBox="0 0 29 29" aria-hidden="true">
        <rect width="29" height="29" fill="#8c8d8f"/>
        <path d="M10 6 l3 0 l1.5 5 l-2 1.5 c1 2.5 2.5 4 5 5 l1.5 -2 l5 1.5 l0 3 c-8 1 -15 -6 -14 -14z" fill="#333436"/>
      </svg>
      <span>(555) 214-7730</span>
    </div>
    <div class="brand">
      <div class="brand__mark"></div>
      <div class="brand__name">REX MORTON<br>CONSTRUCTION, LLC</div>
    </div>
    <div class="band" role="img" aria-label="Decorative band of overlapping grey angular shapes"></div>
    <div class="details">
      <p class="details__name">Rex Morton</p>
      <p class="details__title">(Licensed Contractor, Certified Home Inspector)</p>
      <p class="details__email">Mail ID: Rmorton_Construction@quellbox.example</p>
      <p class="details__services">Remodeling / Roofs / Siding / Drywall / Decks /<br>Pole Barns / New Construction "Serving Southwest Michigan"</p>
    </div>
  </section>
</body>
</html>
```